Business Card Design for ClearPathVitality

We need the new logo on a business card for 3 employees:
Nora Kettering, PhD, Advanced Instructor and Practitioner of SomaLink Integral Medicine (email: nora@clearpathvitality.com)
Ray Holm, Business Manager (email: ray@clearpathvitality.com)
Bea Marlowe, Administrative Assistant (email: bea@helixsense.com)

Target Market(s)

healthcare professionals

Industry/Entity Type

Alternative Medicine

Contact Information for Business Card

Names, titles, emails (names, titles, emails are in project description), phone, address, website, with logo and tagline. See below for address, phone, website: 418 Alder Ln, Bldg 12, Ste 305
Santa Cruz, CA 95060
831-555-2746
www.clearpathvitality.com
Tagline: Roots of Balance, Light of Renewal

Font styles to use
Other font styles liked:
• Gabriela

Colors
00a990
86cfc6
6b449b
b7a5cd
85abd2
abd036

Requirements
Must have
• Colors and style that match the logo design - shades such as blue, green, purple
• Compatible or same font as in the logo
Nice to have
• Nice if it goes with the theme of Nora's last business card - uploaded below
Should not have
• colors or style in conflict with the logo

```html
<!DOCTYPE html>
<html lang="en">
<head>
<meta charset="utf-8">
<title>ClearPathVitality Business Card</title>
<link rel="stylesheet" href="https://fonts.googleapis.com/css2?family=Gabriela&display=swap">
<style>
  :root {
    --page: #dcdcdc;
    --card-top: #2f3f87;
    --card-mid: #3c2a7a;
    --card-bottom: #4f2a7c;
    --white: #ffffff;
    --lime: #b5d334;
    --line: rgba(255,255,255,0.85);
  }
  * { margin: 0; padding: 0; box-sizing: border-box; }
  html, body {
    width: 1200px; height: 1200px; overflow: hidden;
    background: var(--page);
    font-family: "Gabriela", Georgia, serif;
  }
  .canvas { position: relative; width: 1200px; height: 1200px; }
  .card {
    position: absolute; top: 456px; width: 509px; height: 291px;
    background: linear-gradient(180deg, var(--card-top) 0%, var(--card-mid) 50%, var(--card-bottom) 100%);
    color: var(--white);
    overflow: hidden;
  }
  .card-front { left: 47px; }
  .card-back { left: 643px; }
  .texture {
    position: absolute; inset: 0;
    background: radial-gradient(ellipse at 65% 20%, rgba(140,160,220,0.18), transparent 60%);
  }
  .brand { position: absolute; display: flex; align-items: center; }
  .brand-dot { border-radius: 50%; background: var(--white); flex: none; }
  .brand-name { color: var(--white); white-space: nowrap; }
  .card-front .brand { left: 50%; top: 135px; transform: translate(-50%, -50%); gap: 12px; }
  .card-front .brand-dot { width: 80px; height: 80px; }
  .card-front .brand-name { font-size: 28px; }
  .card-back .brand { left: 47px; top: 144px; transform: translateY(-50%); gap: 9px; }
  .card-back .brand-dot { width: 56px; height: 56px; }
  .card-back .brand-name { font-size: 17px; }
  .tagline {
    position: absolute; left: 0; right: 0; text-align: center;
    font-size: 10px; letter-spacing: 3px; text-transform: uppercase;
  }
  .card-front .tagline { top: 192px; }
  .card-back .tagline { top: 266px; }
  .person {
    position: absolute; left: 252px; top: 86px;
    border-left: 1px solid var(--line); padding-left: 7px;
  }
  .person-name { font-size: 16px; letter-spacing: 1.5px; text-transform: uppercase; line-height: 1.1; }
  .person-title { font-size: 7.5px; color: var(--lime); text-transform: uppercase; line-height: 1.3; margin-top: 3px; }
  .contact {
    position: absolute; left: 252px; top: 148px;
    border-left: 1px solid var(--line); padding-left: 3px;
    list-style: none;
  }
  .contact li {
    display: flex; align-items: center; gap: 5px;
    height: 14.6px; font-size: 7.5px; color: var(--lime); white-space: nowrap;
  }
  .contact svg { width: 9px; height: 9px; flex: none; }
</style>
</head>
<body>
<main class="canvas">
  <section class="card card-front">
    <div class="texture" role="img" aria-label="Faint DNA helix pattern"></div>
    <div class="brand">
      <span class="brand-dot"></span>
      <span class="brand-name">ClearPathVitality</span>
    </div>
    <p class="tagline">Roots of Balance, Light of Renewal</p>
  </section>

  <section class="card card-back">
    <div class="texture" role="img" aria-label="Faint DNA helix pattern"></div>
    <div class="brand">
      <span class="brand-dot"></span>
      <span class="brand-name">ClearPathVitality</span>
    </div>
    <div class="person">
      <h1 class="person-name">Nora Kettering</h1>
      <p class="person-title">PhD, Advanced Instructor and Practitioner<br>of SomaLink Integral Medicine</p>
    </div>
    <ul class="contact">
      <li>
        <svg viewBox="0 0 10 10"><path d="M5 0.5a3.3 3.3 0 0 0-3.3 3.3C1.7 6.3 5 9.5 5 9.5s3.3-3.2 3.3-5.7A3.3 3.3 0 0 0 5 .5z" fill="#fff"/><circle cx="5" cy="3.8" r="1.2" fill="#3c2a7a"/></svg>
        418 Alder Ln, Bldg 12, Ste 305 Santa Cruz, CA 95060
      </li>
      <li>
        <svg viewBox="0 0 10 10"><path d="M2.2 0.8l1.6 2-1 1.1c.6 1.3 1.6 2.3 2.9 2.9l1.1-1 2 1.6-1 1.8C4.5 9 1 5.5 .8 1.8z" fill="#fff"/></svg>
        831-555-2746
      </li>
      <li>
        <svg viewBox="0 0 10 10"><rect x="0.7" y="2" width="8.6" height="6" fill="none" stroke="#fff" stroke-width="0.9"/><path d="M0.7 2L5 5.6 9.3 2" fill="none" stroke="#fff" stroke-width="0.9"/></svg>
        nora@clearpathvitality.com
      </li>
      <li>
        <svg viewBox="0 0 10 10" fill="none" stroke="#fff" stroke-width="0.8"><circle cx="5" cy="5" r="4.2"/><ellipse cx="5" cy="5" rx="1.8" ry="4.2"/><path d="M0.8 5h8.4M1.5 2.8h7M1.5 7.2h7"/></svg>
        www.clearpathvitality.com
      </li>
    </ul>
    <p class="tagline">Roots of Balance, Light of Renewal</p>
  </section>
</main>
</body>
</html>
```